Voltline Assemblies, Inc. Business Card

Voltline has three operating entities and I'm looking for a standard business card template that can be used for Voltline and the three operating entities that the logo just get swapped out, but has a very similar look and feel. Ultimately if someone had a business card from each, they assume the organizations are related because they all have the same look and feel.
Below are our websites and I will attached the logos for each entity:
https://www.voltlineassemblies.example/
https://www.brantoceramic.example/
https://www.omra-kfsd.example/
https://www.summitbreaker.example/

Target Market(s)

US Voltline

Industry/Entity Type

US Voltline

Contact Information for Business Card

Normal stuff

```html
<!DOCTYPE html>
<html lang="en">
<head>
<meta charset="utf-8">
<title>Voltline Assemblies, Inc. Business Card</title>
<link href="https://fonts.googleapis.com/css2?family=Montserrat:wght@400;600;800&display=swap" rel="stylesheet">
<style>
  :root {
    --navy: #1f2d66;
    --red: #c8202f;
    --white: #ffffff;
    --ink: #1a1a1a;
    --backdrop: #2b2b2b;
  }
  * { box-sizing: border-box; margin: 0; padding: 0; }
  html, body {
    width: 1200px; height: 900px; overflow: hidden;
    background: var(--backdrop);
    font-family: "Montserrat", Arial, sans-serif;
  }
  .canvas { position: relative; width: 1200px; height: 900px; }
  .card {
    position: absolute; left: 250px;
    width: 700px; height: 400px;
    border-radius: 22px;
    overflow: hidden;
    box-shadow: 0 10px 30px rgba(0,0,0,.45);
  }
  .card--back { top: 40px; background: var(--navy); }
  .card--front { top: 470px; background: var(--white); }

  .brand {
    position: absolute; left: 0; right: 0;
    display: flex; align-items: center; justify-content: center; gap: 18px;
  }
  .brand__dot { width: 56px; height: 56px; border-radius: 50%; flex: none; }
  .brand__name {
    font-weight: 800; font-size: 40px; letter-spacing: .5px; line-height: 1.1;
    white-space: nowrap;
  }
  .card--back .brand { top: 165px; }
  .card--back .brand__dot { background: var(--white); }
  .card--back .brand__name { color: var(--white); }

  .card--front .brand { top: 60px; }
  .card--front .brand__dot { background: var(--navy); }
  .card--front .brand__name { color: var(--navy); }

  .person {
    position: absolute; left: 20px; top: 200px; width: 282px; text-align: right;
  }
  .person__name {
    color: var(--navy); font-weight: 800; font-size: 32px; letter-spacing: .5px;
    white-space: nowrap;
  }
  .person__title { color: var(--ink); font-size: 22px; margin-top: 4px; }
  .divider {
    position: absolute; left: 320px; top: 200px;
    width: 3px; height: 74px; background: var(--red);
  }
  .contact {
    position: absolute; left: 340px; top: 198px;
    list-style: none; color: var(--ink); font-size: 16px;
  }
  .contact li {
    display: flex; align-items: center; gap: 8px; height: 26px; white-space: nowrap;
  }
  .contact svg { width: 16px; height: 16px; flex: none; }
  .address {
    position: absolute; left: 0; right: 0; top: 320px;
    text-align: center; color: var(--ink); font-size: 20px;
  }
</style>
</head>
<body>
<main class="canvas">
  <section class="card card--back" aria-label="Card back">
    <div class="brand">
      <span class="brand__dot"></span>
      <span class="brand__name">Voltline Assemblies, Inc.</span>
    </div>
  </section>

  <section class="card card--front" aria-label="Card front">
    <div class="brand">
      <span class="brand__dot"></span>
      <span class="brand__name">Voltline Assemblies, Inc.</span>
    </div>

    <div class="person">
      <p class="person__name">DARREN COLE</p>
      <p class="person__title">Director</p>
    </div>
    <div class="divider"></div>

    <ul class="contact">
      <li>
        <svg viewBox="0 0 16 16" aria-hidden="true"><rect x="4" y="1" width="8" height="14" rx="1.5" fill="none" stroke="#1f2d66" stroke-width="1.5"/><circle cx="8" cy="12.5" r="0.9" fill="#1f2d66"/></svg>
        555-014-2290
      </li>
      <li>
        <svg viewBox="0 0 16 16" aria-hidden="true"><rect x="1" y="3.5" width="14" height="9" fill="#1f2d66"/><path d="M1 3.5 L8 9 L15 3.5" fill="none" stroke="#fff" stroke-width="1.2"/></svg>
        info@voltlineassemblies.example
      </li>
      <li>
        <svg viewBox="0 0 16 16" aria-hidden="true"><circle cx="8" cy="8" r="6.5" fill="none" stroke="#1f2d66" stroke-width="1.3"/><ellipse cx="8" cy="8" rx="3" ry="6.5" fill="none" stroke="#1f2d66" stroke-width="1"/><path d="M1.5 8 H14.5 M2.5 5 H13.5 M2.5 11 H13.5" stroke="#1f2d66" stroke-width="1"/></svg>
        www.voltlineassemblies.example
      </li>
    </ul>

    <p class="address">2140 W Harlan, Brookfield, Kansas 66010</p>
  </section>
</main>
</body>
</html>
```